Australian classical music tour in Europe

We need a poster to advertise our concerts in Europe in April and May. It will be put up in concert halls and churches and online, so it should be suitable for print in colour and black and white, and also look very good on a website.

The title of the concerts is "The Glow of Merrowind".

We will have to overlay the poster with extra information, specific to each venue, so there needs to be space for dates and times and locations to be added.

We are a group of five musicians from Sydney, Australia, playing piano, harp, flute, clarinet, and viola. We would like to see a harp, flute and clarinet, in the poster, and others of those instruments can be used. Do not use any instruments except those. In most of our photos, you can see our instruments already.

Our logo is attached in both black and in gold - please make this logo prominent.

The mood of the poster should definitely be light and friendly, and should show the idea of beautiful classical music.

As we are from Australia we should see images of Australia which could include buildings, landscape, and especially animals like the kangaroo, koala, kookaburra or similar. It could also include Aboriginal people or paintings (for example, dot paintings or cave paintings. One painting with dots appears in the photo of the viola player).

Also, I have some excellent photos of the musicians, we aim to have all five people included.

I know there are a lot of suggested elements - but I think the best poster will not be cluttered too much.

Industry/Entity Type

Online

Requirements
Must have
• Images of music and of Australia
• Title, "The Glow of Merrowind"
Nice to have
• Photos of the five musicians is ideal.
Should not have
• Do not include instruments that are not in the list - harp flute clarinet viola piano.

```html
<!DOCTYPE html>
<html lang="en">
<head>
<meta charset="utf-8">
<title>The Glow of Merrowind – The Lanternfield Ensemble</title>
<link rel="stylesheet" href="https://fonts.googleapis.com/css2?family=Oswald:wght@500;600&display=swap">
<style>
  :root {
    --paper: #eef0ef;
    --navy: #2a2f8f;
    --pink: #ec4f82;
    --cyan: #35b8ea;
    --yellow: #f3e23a;
    --green: #3fe07c;
    --gold: #c49a3c;
    --photo-warm: #b98a6c;
    --photo-deep: #5a3a2c;
  }
  html, body {
    margin: 0;
    padding: 0;
    overflow: hidden;
    background: var(--paper);
  }
  .poster {
    position: relative;
    width: 813px;
    height: 1200px;
    overflow: hidden;
    background: var(--paper);
    font-family: "Oswald", "Arial Narrow", sans-serif;
  }
  .stripes {
    position: absolute;
    inset: 0;
    width: 813px;
    height: 1200px;
  }
  .top-band, .bottom-band {
    position: absolute;
    left: 0;
    width: 813px;
    background: var(--navy);
  }
  .top-band { top: 0; height: 10px; }
  .bottom-band { bottom: 0; height: 46px; }
  .landmark {
    position: absolute;
    left: 100px;
    top: 200px;
    width: 430px;
    height: 150px;
    border-radius: 60% 60% 4px 4px / 90% 90% 4px 4px;
    background: linear-gradient(180deg, rgba(236,79,130,0.10), rgba(236,79,130,0.28));
  }
  .ensemble-name {
    position: absolute;
    top: 56px;
    left: 262px;
    margin: 0;
    font-weight: 600;
    font-size: 25px;
    letter-spacing: 0.5px;
    color: var(--gold);
    text-transform: uppercase;
    white-space: nowrap;
  }
  .title {
    position: absolute;
    right: 122px;
    top: 92px;
    margin: 0;
    font-weight: 600;
    text-align: right;
    line-height: 0.98;
    text-transform: uppercase;
  }
  .title span { display: block; }
  .title .pink { color: var(--pink); font-size: 112px; }
  .title .cyan { color: var(--cyan); font-size: 112px; }
  .title .place { font-size: 132px; letter-spacing: 1px; }
  .musicians {
    position: absolute;
    top: 545px;
    left: 0;
    width: 813px;
    height: 165px;
  }
  .musician {
    position: absolute;
    top: 0;
    width: 162px;
    height: 162px;
    border-radius: 50%;
  }
  .musician.duo { left: 24px; background: radial-gradient(circle at 50% 45%, #a88a72, #5c4a3c); }
  .musician.viola { left: 235px; background: radial-gradient(circle at 50% 45%, #c9a27a, #7a3c22); }
  .musician.piano { left: 441px; background: radial-gradient(circle at 50% 45%, #e6cfc3, #b84a4a); }
  .musician.harp { left: 631px; background: radial-gradient(circle at 50% 50%, #8a6a4a, #2a1a14); }
  .venue-details {
    position: absolute;
    top: 722px;
    left: 268px;
    margin: 0;
    font-weight: 600;
    font-size: 120px;
    line-height: 0.97;
    color: var(--green);
    text-transform: uppercase;
  }
  .venue-details span { display: block; }
</style>
</head>
<body>
<main class="poster">
  <div class="top-band"></div>

  <svg class="stripes" viewBox="0 0 813 1200" aria-hidden="true">
    <g class="stripes-left">
      <rect x="0" y="28" width="105" height="17" fill="var(--cyan)"/>
      <rect x="0" y="62" width="230" height="17" fill="var(--pink)"/>
      <rect x="0" y="96" width="340" height="17" fill="var(--yellow)"/>
      <rect x="0" y="130" width="510" height="17" fill="var(--cyan)"/>
      <rect x="0" y="164" width="380" height="17" fill="var(--pink)"/>
      <rect x="0" y="198" width="320" height="17" fill="var(--yellow)"/>
      <rect x="0" y="232" width="360" height="17" fill="var(--pink)"/>
      <rect x="0" y="266" width="400" height="17" fill="var(--cyan)"/>
      <rect x="0" y="300" width="420" height="17" fill="var(--pink)"/>
      <rect x="0" y="334" width="500" height="17" fill="var(--yellow)"/>
      <rect x="0" y="368" width="480" height="17" fill="var(--cyan)"/>
      <rect x="0" y="402" width="190" height="17" fill="var(--pink)"/>
      <rect x="0" y="436" width="130" height="17" fill="var(--yellow)"/>
      <rect x="0" y="470" width="160" height="17" fill="var(--cyan)"/>
    </g>
    <g class="stripes-right">
      <rect x="460" y="16" width="353" height="17" fill="var(--yellow)"/>
      <rect x="630" y="62" width="183" height="17" fill="var(--pink)"/>
      <rect x="680" y="96" width="133" height="17" fill="var(--cyan)"/>
      <rect x="720" y="130" width="93" height="17" fill="var(--yellow)"/>
      <rect x="700" y="164" width="113" height="17" fill="var(--pink)"/>
      <rect x="740" y="198" width="73" height="17" fill="var(--cyan)"/>
      <rect x="690" y="232" width="123" height="17" fill="var(--yellow)"/>
      <rect x="760" y="266" width="53" height="17" fill="var(--pink)"/>
      <rect x="720" y="300" width="93" height="17" fill="var(--cyan)"/>
      <rect x="700" y="334" width="113" height="17" fill="var(--pink)"/>
      <rect x="740" y="368" width="73" height="17" fill="var(--yellow)"/>
      <rect x="690" y="402" width="123" height="17" fill="var(--cyan)"/>
      <rect x="720" y="436" width="93" height="17" fill="var(--pink)"/>
      <rect x="660" y="470" width="153" height="17" fill="var(--cyan)"/>
    </g>
    <g class="detail-bars-left" fill="var(--green)">
      <rect x="0" y="792" width="148" height="20"/>
      <rect x="0" y="824" width="200" height="20"/>
      <rect x="0" y="856" width="170" height="20"/>
      <rect x="0" y="888" width="212" height="20"/>
      <rect x="0" y="920" width="190" height="20"/>
      <rect x="0" y="952" width="126" height="20"/>
      <rect x="0" y="986" width="158" height="20"/>
      <rect x="0" y="1018" width="116" height="20"/>
    </g>
    <g class="detail-bars-right" fill="var(--green)">
      <rect x="700" y="782" width="113" height="20"/>
      <rect x="740" y="814" width="73" height="20"/>
      <rect x="690" y="846" width="123" height="20"/>
      <rect x="760" y="878" width="53" height="20"/>
      <rect x="650" y="910" width="163" height="20"/>
      <rect x="720" y="942" width="93" height="20"/>
      <rect x="636" y="974" width="177" height="20"/>
      <rect x="700" y="1006" width="113" height="20"/>
      <rect x="672" y="1038" width="141" height="20"/>
    </g>
  </svg>

  <div class="landmark" role="img" aria-label="Faint silhouette of a Sydney harbour landmark"></div>

  <p class="ensemble-name">The Lanternfield Ensemble</p>

  <h1 class="title">
    <span class="pink">The</span>
    <span class="cyan">Glow</span>
    <span class="pink">Of</span>
    <span class="cyan place">Merrowind</span>
  </h1>

  <section class="musicians" aria-label="The musicians">
    <div class="musician duo" role="img" aria-label="Photo of the flute and clarinet players"></div>
    <div class="musician viola" role="img" aria-label="Photo of the viola player before a dot painting"></div>
    <div class="musician piano" role="img" aria-label="Photo of the pianist"></div>
    <div class="musician harp" role="img" aria-label="Photo of the harpist on stage"></div>
  </section>

  <p class="venue-details">
    <span>Other</span>
    <span>Details</span>
    <span>Here :)</span>
  </p>

  <div class="bottom-band"></div>
</main>
</body>
</html>
```